Simple Website Design for Law Office

I need a website design for our law office (Law Offices of Marcus Trell) that is extremely simple, only including a landing page and perhaps a contact page (parallax scrolling).

Website should look similar to this one (template): https://www.quorvabellwith.com/

Design should be modern, simple, and inviting. There are a few assets like logo, stock photos/icons we would like added as well, and some language and contact info, but very basic stuff.

The name of the company is: Law Offices of Marcus Trell

Target Market(s)

B2B corporate clients, users from Canada, UK, East Asia, and all potential users with immigration needs

Coding

Number of Pages Required

2 page

Colors

Designer to choose colors to be used in the design.

Requirements
Must have
• Landing page, Contact Page
• Simple, elegant design with minimalist font
Nice to have
• Parallax scrolling, so one page and can scroll to contact us segment

```html
<!DOCTYPE html>
<html lang="en">
<head>
<meta charset="utf-8">
<title>Law Offices of Marcus Trell</title>
<link rel="stylesheet" href="https://fonts.googleapis.com/css2?family=Open+Sans:wght@400;600;700&family=Raleway:wght@300;400&display=swap">
<style>
:root{
  --white:#ffffff;
  --ink:#1c1c1c;
  --muted:#8a8a8a;
  --soft:#f4f4f4;
  --line:#dcdcdc;
  --accent:#f58a3c;
  --navy:#2f3640;
  --icon:#bdbdbd;
  --hero-top:#3a3d42;
  --hero-bottom:#2a2620;
  --map-a:#d3dccb;
  --map-b:#dedad3;
}
*{margin:0;padding:0;box-sizing:border-box}
html,body{width:1200px;height:2765px;overflow:hidden}
body{position:relative;background:var(--white);font-family:"Open Sans",Arial,sans-serif;color:var(--ink)}
.abs{position:absolute}
section,header,footer{position:absolute;left:0;width:1200px}

.hero{top:0;height:609px;color:var(--white);
  background:radial-gradient(ellipse at 75% 35%,#5b5f63 0%,transparent 55%),
  linear-gradient(180deg,var(--hero-top) 0%,#46484a 40%,#4a3f33 65%,var(--hero-bottom) 100%)}
.hero-photo{position:absolute;inset:0}
.brand{left:135px;top:14px;font-family:"Raleway",sans-serif;font-weight:300;font-size:36px;line-height:40px;letter-spacing:2px}
.nav{top:17px;font-size:19px}
.nav a{color:var(--white);text-decoration:none;position:absolute;white-space:nowrap}
.hero-kicker{left:126px;top:228px;font-family:"Raleway",sans-serif;font-size:30px;font-weight:400}
.hero-title{left:124px;top:250px;font-family:"Raleway",sans-serif;font-size:66px;font-weight:400;white-space:nowrap}
.hero-rule{left:130px;top:337px;width:55px;height:2px;background:var(--white)}
.hero-text{left:128px;top:359px;width:420px;font-size:13.5px;line-height:20px;color:#dcdcdc}

.social{top:609px;height:91px;border-bottom:2px solid var(--line)}
.social h3{left:129px;top:15px;font-size:17px;font-weight:600}
.social p{left:130px;top:40px;font-size:12px;line-height:17px;color:var(--muted)}
.social-links{top:25px;left:785px;display:flex;gap:22px}
.social-link{display:flex;align-items:center;gap:6px;font-size:13px;color:var(--icon);font-weight:600}
.social-link i{width:12px;height:12px;background:var(--icon);display:block}

.tabs{top:700px;height:509px;background:var(--soft)}
.tabs h3{left:304px;top:128px;font-size:18px;font-weight:600}
.body-text{font-size:12.5px;line-height:17px;color:var(--muted)}
.tab-label{left:151px;top:356px;font-size:12px;color:var(--white)}

.services{top:1209px;height:511px}
.services h3{left:665px;top:90px;font-size:18px;font-weight:600}
.accent-rule{height:2px;width:55px;background:var(--accent)}
.item-dot{width:34px;height:34px;border:2px solid var(--accent);border-radius:50%}
.item-title{font-size:12px;font-weight:600}

.office{top:1720px;height:451px;background:linear-gradient(90deg,var(--map-a) 0%,var(--map-b) 100%)}
.office-map{position:absolute;inset:0}
.office-band{top:0;left:0;width:1200px;height:225px;background:rgba(40,40,40,.86);color:var(--white);font-family:"Raleway",sans-serif;font-weight:300}
.office-band h2{left:0;width:1200px;text-align:center;top:24px;font-size:30px;font-weight:400}
.office-rule{left:573px;top:66px;width:55px;height:2px;background:var(--white)}
.office-col{top:70px;font-size:18px;line-height:28px;white-space:nowrap}
.office-col.left{right:638px;text-align:right}
.office-col.right{left:638px}

.contact{top:2171px;height:524px}
.contact h2{left:0;width:1200px;text-align:center;top:84px;font-family:"Raleway",sans-serif;font-weight:400;font-size:32px}
.contact .accent-rule{left:573px;top:140px}
.contact-lead{left:0;width:1200px;text-align:center;top:166px;font-size:12px;color:var(--muted)}
.field{border-bottom:1px solid var(--line);font-size:11.5px;color:#a8a8a8;padding-left:10px;height:22px}
.send{left:537px;top:416px;width:126px;height:38px;background:var(--navy);color:var(--white);font-size:13px;font-weight:600;display:flex;align-items:center;justify-content:center}

.footer{top:2695px;height:70px;background:var(--navy);color:#c9ccd1}
.footer-links{left:0;width:1200px;top:14px;display:flex;justify-content:center;gap:18px}
.footer-links i{width:14px;height:14px;border-radius:50%;background:#c9ccd1;display:block}
.copyright{left:0;width:1200px;top:44px;text-align:center;font-size:10px;font-weight:700}
</style>
</head>
<body>

<header class="hero">
  <div class="hero-photo" role="img" aria-label="Photograph of a city skyline at dusk seen from above"></div>
  <div class="abs brand">Law Offices<br>of Marcus Trell</div>
  <nav class="abs nav">
    <a style="left:816px">Home</a>
    <a style="left:905px">Services</a>
    <a style="left:1012px">Contact</a>
  </nav>
  <div class="abs hero-kicker">WE ARE</div>
  <h1 class="abs hero-title">a Law Office</h1>
  <div class="abs hero-rule"></div>
  <p class="abs hero-text">Lorem ipsum dolor sit amet, consectetur adipiscing elit. Aenean euismod bibendum laoreet. Proin gravida dolor sit amet lacus accumsan et viverra justo commodo.</p>
</header>

<section class="social">
  <h3 class="abs">Social Media</h3>
  <p class="abs">Lorem ipsum dolor sit amet, consectetur adipiscing elit.<br>Aenean euismod bibendum laoreet.</p>
  <div class="abs social-links">
    <span class="social-link"><i></i>Page</span>
    <span class="social-link"><i></i>Feed</span>
    <span class="social-link"><i></i>Posts</span>
    <span class="social-link"><i></i>Photos</span>
  </div>
</section>

<section class="tabs">
  <h3 class="abs">Tabs with parallax effect.</h3>
  <p class="abs body-text" style="left:304px;top:192px;width:420px">Lorem ipsum dolor sit amet, consectetur adipiscing elit. Aenean euismod bibendum laoreet. Proin gravida dolor sit amet lacus accumsan et viverra justo commodo. Proin sodales pulvinar tempor. Cum sociis natoque penatibus et magnis dis parturient montes.</p>
  <p class="abs body-text" style="left:304px;top:277px;width:420px">Lorem ipsum dolor sit amet, consectetur adipiscing elit. Aenean euismod bibendum laoreet.</p>
  <div class="abs tab-label">TAB 3</div>
  <svg class="abs" style="left:850px;top:112px" width="168" height="172" viewBox="0 0 168 172" fill="none" stroke="#111" stroke-width="7" stroke-linejoin="round" aria-label="Courthouse icon">
    <path d="M6 55 L84 5 L162 55 V68 H6 Z"/>
    <circle cx="84" cy="40" r="11"/>
    <rect x="16" y="82" width="18" height="62"/>
    <rect x="54" y="82" width="18" height="62"/>
    <rect x="96" y="82" width="18" height="62"/>
    <rect x="134" y="82" width="18" height="62"/>
    <path d="M6 154 H162 M2 166 H166"/>
  </svg>
</section>

<section class="services">
  <svg class="abs" style="left:188px;top:141px" width="173" height="154" viewBox="0 0 173 154" fill="none" stroke="#111" stroke-width="7" stroke-linejoin="round" aria-label="Briefcase icon">
    <rect x="4" y="26" width="165" height="124" rx="4"/>
    <path d="M62 26 V6 H111 V26"/>
    <path d="M4 32 L70 78 M169 32 L103 78"/>
    <rect x="70" y="70" width="33" height="34"/>
  </svg>
  <h3 class="abs">Services list section</h3>
  <div class="abs accent-rule" style="left:684px;top:131px"></div>
  <p class="abs body-text" style="left:684px;top:156px;width:380px">Lorem ipsum dolor sit amet, consectetur adipiscing elit. Aenean euismod bibendum laoreet. Proin gravida dolor sit amet lacus accumsan et viverra justo commodo.</p>
  <div class="abs item-dot" style="left:684px;top:246px"></div>
  <div class="abs item-title" style="left:745px;top:243px">Title</div>
  <p class="abs body-text" style="left:745px;top:264px;width:330px">Lorem ipsum dolor sit amet, consectetur adipiscing elit. Aenean euismod bibendum laoreet.</p>
  <div class="abs item-dot" style="left:684px;top:330px"></div>
  <div class="abs item-title" style="left:745px;top:327px">Title</div>
  <p class="abs body-text" style="left:745px;top:348px;width:330px">Lorem ipsum dolor sit amet, consectetur adipiscing elit. Aenean euismod bibendum laoreet. Proin gravida dolor sit amet lacus accumsan et viverra justo commodo.</p>
</section>

<section class="office">
  <div class="office-map" role="img" aria-label="Street map of the area around the office"></div>
  <div class="abs office-band">
    <h2 class="abs">OUR OFFICE</h2>
    <div class="abs office-rule"></div>
    <div class="abs office-col left">Phone:<br>(0145) 555-0192<br>Hours<br>Monday - Friday</div>
    <div class="abs office-col right">Location:<br>780 Linden Crest avenue<br>Harbor Vale, CA 9041<br>9 am - 17 pm</div>
  </div>
</section>

<section class="contact">
  <h2 class="abs">CONTACT US</h2>
  <div class="abs accent-rule"></div>
  <p class="abs contact-lead">Lorem ipsum dolor sit amet, consectetur adipiscing elit.</p>
  <div class="abs field" style="left:120px;top:254px;width:453px">Name</div>
  <div class="abs field" style="left:120px;top:306px;width:453px">Email</div>
  <div class="abs field" style="left:120px;top:358px;width:453px">Subject</div>
  <div class="abs field" style="left:630px;top:254px;width:452px;height:127px">Message</div>
  <div class="abs send">Send Message</div>
</section>

<footer class="footer">
  <div class="abs footer-links"><i></i><i></i><i></i><i></i><i></i><i></i><i></i></div>
  <div class="abs copyright">© 2019 Trell Law</div>
</footer>

</body>
</html>
```